The Quillon Hood - Packaging design and logo

I am looking for a packaging design for a product. The product is a bottle cap that reminds you of a condom. I am looking for both a design for the box as well as the condom wrap. The box will contain 4 condoms and a manual how to use the bottle cap.
I do not have a logo, ideas that are set on the box are very appreciated.

Target Market(s)

gift ideas

Industry/Entity Type

Gift Shop

Logo Text

The Quillon Hood - Extra time for you wine

Logo styles of interest
Pictorial/Combination Logo
Wordmark Logo
Font styles to use
Serif

Colors
eda3c7
000000
ffffff

Requirements
Must have
• Humor, simple and smart.
• I would like it to be an experience opening the box.
• 1. The wrap around the box (same picture and logo as the box itself)
• 2. The box.
• 3. Inside the box.
• 4. The condom wrappers
• -----------
• The logo: a simply one line drawing of a bottle ( tilted a little) with a condom around to top.
Nice to have
• Very simple but eye catching product.
• Great for a gift.
• packaging to be reminded of something "expensive".
Should not have
• Many different fonts.
• Harsh colors.
• unclassy

```html
<!DOCTYPE html>
<html lang="en">
<head>
<meta charset="utf-8">
<title>The Quillon Hood - Extra time for you wine</title>
<link rel="stylesheet" href="https://fonts.googleapis.com/css2?family=Montserrat:ital,wght@0,300;0,700;1,300;1,700;1,800&display=swap">
<style>
  :root {
    --canvas-bg: #f5f5f7;
    --pink: #f22fae;
    --pink-soft: #f45cc0;
    --purple: #7447ad;
    --purple-deep: #6a3aa3;
    --wrapper-purple: #5a2a98;
    --wrapper-crimp: #4a1f86;
    --white: #ffffff;
  }
  * { margin: 0; padding: 0; box-sizing: border-box; }
  html, body { width: 1200px; height: 800px; overflow: hidden; background: var(--canvas-bg); }
  .canvas { position: relative; width: 1200px; height: 800px; font-family: "Montserrat", sans-serif; }

  .box {
    position: absolute; left: 114px; top: 166px; width: 462px; height: 460px;
    border-radius: 5px; overflow: hidden; background: var(--purple);
  }
  .box-art { position: absolute; inset: 0; width: 100%; height: 100%; }
  .pattern-area { position: absolute; left: 0; top: 0; width: 462px; height: 220px; }

  .tagline {
    position: absolute; right: 36px; top: 38px; text-align: right;
    color: var(--white); font-style: italic; font-size: 43px; line-height: 54px;
    font-weight: 800; letter-spacing: -0.5px;
  }
  .tagline .light { font-weight: 300; }

  .count {
    position: absolute; left: 300px; top: 262px; width: 100px; text-align: center;
    color: var(--white); font-style: italic; font-weight: 800; font-size: 104px; line-height: 1;
  }
  .wordmark {
    position: absolute; right: 24px; top: 368px;
    color: var(--pink); font-style: italic; font-weight: 300; font-size: 30px;
  }

  .illustration {
    position: absolute; left: 54px; top: 154px; width: 172px; height: 272px;
    border-radius: 8px;
    background: linear-gradient(180deg, rgba(255,255,255,0.18), rgba(242,47,174,0.55));
  }

  .wrapper {
    position: absolute; left: 680px; top: 186px; width: 418px; height: 420px;
    overflow: hidden;
    background: radial-gradient(circle at 50% 45%, #4e2288 0%, var(--wrapper-purple) 45%, #6a35ab 100%);
  }
  .wrapper-pattern {
    position: absolute; inset: 30px;
    background: linear-gradient(155deg, rgba(242,47,174,0.10), rgba(242,47,174,0.22) 50%, rgba(242,47,174,0.10));
  }
  .wrapper-crimp { position: absolute; inset: 0; width: 100%; height: 100%; }
  .wrapper-name {
    position: absolute; color: var(--pink); font-weight: 300; font-size: 28px;
    white-space: nowrap; transform: rotate(-25deg); transform-origin: left bottom;
  }
  .wrapper-name.upper { left: 236px; top: 112px; }
  .wrapper-name.lower { left: 132px; top: 366px; }
  .wrapper-name.edge-left { left: -64px; top: 204px; }
  .wrapper-name.edge-right { left: 356px; top: 392px; }
</style>
</head>
<body>
<main class="canvas">
  <section class="box" aria-label="Box front">
    <svg class="box-art" viewBox="0 0 462 460" aria-hidden="true">
      <rect x="0" y="0" width="462" height="300" fill="var(--pink)"/>
      <path d="M0,232 C70,212 140,214 220,232 S380,262 462,246 L462,460 L0,460 Z" fill="var(--purple)"/>
      <rect x="0" y="428" width="462" height="32" fill="var(--purple-deep)"/>
      <line x1="0" y1="427" x2="462" y2="427" stroke="var(--white)" stroke-width="3"/>
    </svg>
    <div class="pattern-area" role="img" aria-label="Pink zigzag chevron pattern"></div>
    <div class="illustration" role="img" aria-label="Line drawing of a wine bottle with a hood over its neck beside a glass of wine"></div>
    <h1 class="tagline"><span class="light">EXTRA</span> TIME<br>FOR YOUR<br>WINE</h1>
    <p class="count">4</p>
    <p class="wordmark">quillonhood</p>
  </section>

  <section class="wrapper" aria-label="Foil wrapper">
    <div class="wrapper-pattern" role="img" aria-label="Repeating pattern of tilted hooded wine bottles"></div>
    <span class="wrapper-name upper">quillonhood</span>
    <span class="wrapper-name lower">quillonhood</span>
    <span class="wrapper-name edge-left">quillonhood</span>
    <span class="wrapper-name edge-right">quillonhood</span>
    <svg class="wrapper-crimp" viewBox="0 0 418 420" aria-hidden="true">
      <g stroke="var(--wrapper-crimp)" stroke-width="16" stroke-dasharray="2 3" fill="none">
        <line x1="0" y1="8" x2="418" y2="8"/>
        <line x1="0" y1="412" x2="418" y2="412"/>
        <line x1="8" y1="0" x2="8" y2="420"/>
        <line x1="410" y1="0" x2="410" y2="420"/>
      </g>
      <rect x="30" y="30" width="358" height="360" rx="6" fill="none" stroke="rgba(255,255,255,0.08)" stroke-width="2"/>
    </svg>
  </section>
</main>
</body>
</html>
```